Bref créative
Business Card for "Homeward by Plan"
Business card for senior move management company
Simple
Dalia Fenwick
Owner / CEO
Maple Brook, OH
dalia@homeplanex.com
www.homeplanex.com
Relocation | Organizing | Interior Design
Attached is the file for the homeward by plan business cards
png logo file for homewrd by plan
jpeg for homeward by plan business cards

```html
<!DOCTYPE html>
<html lang="en">
<head>
<meta charset="utf-8">
<title>Homeward by Plan — Business Cards</title>
<link rel="stylesheet" href="https://fonts.googleapis.com/css2?family=Open+Sans:wght@400;600&display=swap">
<style>
  :root {
    --backdrop: #2c2c2e;
    --card-green: #7fb79a;
    --card-green-deep: #72ab8d;
    --ink-light: #ffffff;
    --ink-soft: #eef6f1;
  }
  html, body {
    margin: 0;
    padding: 0;
    width: 1200px;
    height: 866px;
    overflow: hidden;
    background: var(--backdrop);
    font-family: "Open Sans", Arial, sans-serif;
  }
  .canvas {
    position: relative;
    width: 1200px;
    height: 866px;
  }
  .card {
    position: absolute;
    background: radial-gradient(ellipse at center, var(--card-green) 0%, var(--card-green-deep) 100%);
    color: var(--ink-light);
    box-shadow: 0 6px 18px rgba(0,0,0,0.45);
  }
  .card--front { left: 278px; top: 170px; width: 422px; height: 233px; }
  .card--back  { left: 516px; top: 458px; width: 408px; height: 233px; }

  .brand {
    position: absolute;
    display: flex;
    align-items: center;
  }
  .brand__circle {
    border-radius: 50%;
    background: var(--ink-soft);
    flex: none;
  }
  .brand__name {
    font-weight: 600;
    color: var(--ink-light);
    line-height: 1.05;
    letter-spacing: 0.5px;
  }
  .card--front .brand { left: 76px; top: 64px; }
  .card--front .brand__circle { width: 80px; height: 80px; margin-right: 16px; }
  .card--front .brand__name { font-size: 24px; }

  .card--back .brand { left: 46px; top: 40px; }
  .card--back .brand__circle { width: 80px; height: 80px; margin-right: 16px; }
  .card--back .brand__name { font-size: 24px; }

  .holder {
    position: absolute;
    right: 22px;
    top: 16px;
    text-align: right;
    font-size: 12px;
    line-height: 1.45;
  }
  .location {
    position: absolute;
    right: 22px;
    top: 186px;
    font-size: 10px;
  }
  .contact-line {
    position: absolute;
    left: 0;
    right: 0;
    bottom: 10px;
    text-align: center;
    font-size: 9px;
    letter-spacing: 0.1px;
    white-space: nowrap;
  }
  .services {
    position: absolute;
    left: 46px;
    top: 192px;
    font-size: 14px;
    letter-spacing: 0.3px;
    margin: 0;
    padding: 0;
    list-style: none;
    display: flex;
    gap: 10px;
  }
  .services li::before {
    content: "•";
    margin-right: 6px;
  }
</style>
</head>
<body>
<main class="canvas">
  <section class="card card--front" aria-label="Business card front">
    <div class="holder">
      <div class="holder__name">Dalia Fenwick</div>
      <div class="holder__title">CEO</div>
    </div>
    <div class="brand">
      <span class="brand__circle" aria-hidden="true"></span>
      <span class="brand__name">Homeward<br>by Plan</span>
    </div>
    <div class="location">Maple Brook, OH</div>
    <div class="contact-line">Ph: 555.203.0142 &nbsp;|&nbsp; Email: dalia@homeplanex.com &nbsp;|&nbsp; Web: www.homeplanex.com</div>
  </section>

  <section class="card card--back" aria-label="Business card back">
    <div class="brand">
      <span class="brand__circle" aria-hidden="true"></span>
      <span class="brand__name">Homeward<br>by Plan</span>
    </div>
    <ul class="services">
      <li>Relocation</li>
      <li>Organizing</li>
      <li>Interior Design</li>
    </ul>
  </section>
</main>
</body>
</html>
```